How likely are people to engage in social distancing? We need a good illustration to show the data!

We surveyed U.S. adults March 20th - 24th, 2020 and asked how likely they were to engage in social distancing (and other COVID-19 related health behaviors). What did the survey find? Basically, most people intend to engage in social distancing behaviors (e.g., avoiding large crowds) and other behaviors that reduce the spread of COVID-19 (e.g., washing hands at least 20 seconds). When most people intend to engage in a behavior, then public health professionals try to leverage that to move more people to act.
Now we need innovative and professional images that attempt to communicate one or all of these findings. The specific findings are nicely summarized in the attached document. For example, 82% of participants intend to engage in social distancing.
What sort of visual are we looking for? Our preference is for an original illustration (or set of illustrations). Our preference is for (creative and powerful illustrations, but we are also open to the creative and well-executed infographics.
We need these images fast . We will award monetary prizes to the 3 best designs. If we like more than that, then we might purchase more (e.g., in past contests, we have purchased as many as 30 designs).
What we will need:
(1) The illustrations must be original and we will need the photoshop and/or illustrator files for all artwork.
(2) You can illustrate all of the findings or just one of them. We need creative approaches that do a lucid job of bringing the data to life. Most people intend to engage in these behaviors. How to communicate that? Corvantists and Halmerites do not differ in their intentions; how to communicate that?
(3) The illustration should say, somewhere: "Based on a survey of 400 U.S. adults conducted March 20 - 24th, 2020."

U.S. Adults

• Original illustrations based on the findings of the survey (see attached document).

```html
<!DOCTYPE html>
<html lang="en">
<head>
<meta charset="utf-8">
<title>How Likely Are People to Engage in Social Distancing?</title>
<link rel="stylesheet" href="https://fonts.googleapis.com/css2?family=Fira+Sans:wght@400;600;700;800;900&display=swap">
<style>
:root{
  --teal:#3fa5c0;
  --teal-deep:#1b8fab;
  --yellow:#fff200;
  --ink:#2a2a2a;
  --white:#ffffff;
  --page:#ffffff;
}
*{box-sizing:border-box;margin:0;padding:0}
html,body{width:1200px;height:1079px;overflow:hidden;background:var(--page)}
body{font-family:"Fira Sans",sans-serif;position:relative}
.poster{position:absolute;left:288px;top:38px;width:615px;height:994px;background:var(--teal);overflow:hidden}
.abs{position:absolute}
.virus{position:absolute;border-radius:50%;background:var(--teal-deep);opacity:.75}
.title{position:absolute;left:0;width:615px;text-align:center;font-weight:900;font-size:35px;line-height:41px;top:28px;color:var(--white);letter-spacing:-.3px;text-shadow:-2px 2px 0 var(--ink),1px -1px 0 var(--ink),-1px -1px 0 var(--ink),1px 1px 0 var(--ink)}
.title .hl{color:var(--yellow)}
.band{position:absolute;left:35px;width:545px;background:var(--yellow);color:var(--ink);text-align:center}
.band strong{display:block;font-weight:700;font-size:14px}
.band span{display:block;font-size:14px;font-weight:400;margin-top:2px}
.band.survey{top:163px;height:69px;padding-top:15px}
.band.compare{top:626px;height:69px;padding-top:16px}
.grid line,.table-lines line{stroke:var(--yellow);stroke-width:1.3;stroke-dasharray:4 4}
.icon{position:absolute;width:70px;height:70px;border-radius:50%;background:radial-gradient(circle at 50% 45%,#e9eef2 0,#ffffff 70%)}
.cell{position:absolute;width:134px;text-align:center;color:var(--white)}
.cell .label{font-size:11.5px;line-height:14.5px;font-weight:400}
.cell .pct{font-size:19px;font-weight:800;color:var(--yellow);line-height:18px}
.cell .sub{font-size:9px;color:var(--yellow);line-height:9px}
.note{position:absolute;left:0;width:615px;text-align:center;color:var(--white);font-size:10.5px;font-weight:600}
.party{position:absolute;width:110px;text-align:center;color:var(--white);font-weight:700;font-size:11px}
.party .dot{display:block;width:22px;height:22px;border-radius:50%;background:var(--white);margin:0 auto 3px}
.row{position:absolute;left:57px;width:520px;height:19px;font-size:12px;font-weight:700;color:var(--white)}
.row.alt{color:var(--yellow)}
.row .v{position:absolute;width:40px;text-align:center;font-size:11px}
.row .r{left:339px}
.row .d{left:448px}
.credit{position:absolute;left:335px;top:960px;width:280px;height:34px;background:var(--yellow);border-top-left-radius:8px;color:var(--ink);font-size:7.6px;font-weight:700;padding:13px 0 0 12px}
</style>
</head>
<body>
<main class="poster">
  <div class="virus" style="left:458px;top:150px;width:24px;height:24px" role="img" aria-label="Virus particle decoration"></div>
  <div class="virus" style="left:158px;top:321px;width:36px;height:36px" role="img" aria-label="Virus particle decoration"></div>
  <div class="virus" style="left:272px;top:510px;width:82px;height:82px" role="img" aria-label="Virus particle decoration"></div>
  <div class="virus" style="left:533px;top:795px;width:56px;height:56px" role="img" aria-label="Virus particle decoration"></div>
  <div class="virus" style="left:65px;top:870px;width:90px;height:90px" role="img" aria-label="Virus particle decoration"></div>

  <h1 class="title">HOW LIKELY<br>ARE PEOPLE TO ENGAGE<br>IN <span class="hl">SOCIAL DISTANCING?</span></h1>

  <header class="band survey">
    <strong>Survey of U.S. Adults (N = 400) conducted March 20th - 24th, 2020</strong>
    <span>Percent of Americans intending to engage in social distancing</span>
  </header>

  <svg class="grid abs" style="left:0;top:0" width="615" height="994">
    <line x1="39" y1="249" x2="39" y2="565"/>
    <line x1="173" y1="249" x2="173" y2="565"/>
    <line x1="307" y1="249" x2="307" y2="565"/>
    <line x1="441" y1="249" x2="441" y2="565"/>
    <line x1="576" y1="249" x2="576" y2="565"/>
    <line x1="39" y1="400" x2="576" y2="400"/>
  </svg>

  <div class="icon" style="left:71px;top:249px" role="img" aria-label="Two people standing apart"></div>
  <div class="icon" style="left:205px;top:251px" role="img" aria-label="Woman working on a laptop at home"></div>
  <div class="icon" style="left:339px;top:253px" role="img" aria-label="Crowd with a prohibition sign"></div>
  <div class="icon" style="left:473px;top:255px" role="img" aria-label="Cancelled toast with a red cross"></div>
  <div class="icon" style="left:70px;top:407px" role="img" aria-label="Three people spaced apart"></div>
  <div class="icon" style="left:204px;top:407px" role="img" aria-label="Hands washing for 20 seconds"></div>
  <div class="icon" style="left:338px;top:407px" role="img" aria-label="Hand sanitizer bottle"></div>
  <div class="icon" style="left:472px;top:407px" role="img" aria-label="Person touching face with prohibition sign"></div>

  <div class="cell" style="left:39px;top:324px"><p class="label">Engage in<br>social distancing</p><p class="pct" style="margin-top:12px">82%</p><p class="sub">intend to</p></div>
  <div class="cell" style="left:173px;top:325px"><p class="label">Work<br>from home</p><p class="pct" style="margin-top:11px">63%</p><p class="sub">intend to</p></div>
  <div class="cell" style="left:307px;top:325px"><p class="label">Avoid<br>large gatherings</p><p class="pct" style="margin-top:11px">85%</p><p class="sub">intend to</p></div>
  <div class="cell" style="left:441px;top:327px"><p class="label">Cancel<br>social activities</p><p class="pct" style="margin-top:9px">81%</p><p class="sub">intend to</p></div>

  <div class="cell" style="left:39px;top:484px"><p class="label">Put distance<br>between yourself<br>and other people</p><p class="pct" style="margin-top:8px">85%</p><p class="sub">intend to</p></div>
  <div class="cell" style="left:175px;top:484px"><p class="label">Wash hands<br>at least<br>20 seconds</p><p class="pct" style="margin-top:8px">87%</p><p class="sub">intend to</p></div>
  <div class="cell" style="left:306px;top:484px"><p class="label">Use hand<br>sanitizer</p><p class="pct" style="margin-top:23px;padding-left:6px">85%</p><p class="sub">intend to</p></div>
  <div class="cell" style="left:440px;top:484px"><p class="label">Avoid touching<br>your eyes,<br>nose, and mouth</p><p class="pct" style="margin-top:8px">81%</p><p class="sub">intend to</p></div>

  <p class="note" style="top:585px">What does this data say? It says that most people intend to engage in these behaviors</p>

  <header class="band compare">
    <strong>Comparing Corvantists and Halmerites</strong>
    <span>March 20th - 24th, 2020 Survey</span>
  </header>

  <svg class="table-lines abs" style="left:0;top:0" width="615" height="994">
    <line x1="362" y1="720" x2="362" y2="923"/>
    <line x1="472" y1="720" x2="472" y2="923"/>
    <line x1="576" y1="720" x2="576" y2="923"/>
    <line x1="39" y1="758" x2="576" y2="758"/>
  </svg>

  <div class="party" style="left:362px;top:715px"><span class="dot"></span>Corvantists</div>
  <div class="party" style="left:470px;top:715px"><span class="dot"></span>Halmerites</div>

  <div class="row" style="top:764px">Engage in social distancing<span class="v r">82%</span><span class="v d">81%</span></div>
  <div class="row alt" style="top:783px">Work from home<span class="v r">60%</span><span class="v d">65%</span></div>
  <div class="row" style="top:802px">Avoid&nbsp; large gatherings<span class="v r">85%</span><span class="v d">84%</span></div>
  <div class="row alt" style="top:821px">Cancel social activities<span class="v r">82%</span><span class="v d">80%</span></div>
  <div class="row" style="top:840px">Put distance between yourself and other people<span class="v r">84%</span><span class="v d">87%</span></div>
  <div class="row alt" style="top:859px">Wash hands at least 20 seconds<span class="v r">87%</span><span class="v d">88%</span></div>
  <div class="row" style="top:878px">Use hand sanitizer<span class="v r">87%</span><span class="v d">84%</span></div>
  <div class="row alt" style="top:896px">Avoid touching your eyes, nose, and mouth<span class="v r">80%</span><span class="v d">82%</span></div>

  <p class="note" style="top:935px">What does this table show? No big differences. Basically the same patterns.</p>

  <footer class="credit">Based on a survey of 400 U.S. adults conducted March 20 - 24th, 2020</footer>
</main>
</body>
</html>
```